Wired Earphone Creative Packaging Design

We would like a creative window box style packaging design for our wired earphone

Size: 6” x 3.5” x 1.5” (enclosed die-cut drawing)
Material: E Flute Paper box
Type: Window Box style
Design features we prefer: friendly, playful, creative, trendy, unique, High tech.
Competitors: Enclosed
Requirement:AI file is preferred

Enclosed are product pictures, marketing materials and competitor designs for your reference.

Any further questions, please feel free to ask.
Updates

So designers get more time to design

Target Market(s)

13-40 Year Olds

Industry/Entity Type

Audio

Colors

Designer to choose colors to be used in the design.

Requirements
Must have
• Window, selling point, creative

```html
<!DOCTYPE html>
<html lang="en">
<head>
<meta charset="utf-8">
<title>Customizable Stereo In-Ear Earphones – Window Box Dieline</title>
<link rel="stylesheet" href="https://fonts.googleapis.com/css2?family=Orbitron:wght@500;600&family=Open+Sans:wght@400;600;700&family=Lora:wght@400&family=Oswald:wght@600&display=swap">
<style>
  :root {
    --paper: #ffffff;
    --cut: #1a1a1a;
    --fold: #6f8fd6;
    --panel-light: #e2e3e7;
    --panel-dark: #4d4d4d;
    --pill: #707070;
    --accent-orange: #f6a21e;
    --accent-yellow: #f7d33a;
    --sky-mid: #62b3e4;
    --sky-edge: #1f4a66;
    --ink: #111111;
    --white: #ffffff;
    --dim: #333333;
  }
  html, body {
    margin: 0;
    padding: 0;
    width: 1200px;
    height: 1000px;
    overflow: hidden;
    background: var(--paper);
  }
  .dieline { display: block; width: 1200px; height: 1000px; }
  .cut { fill: none; stroke: var(--cut); stroke-width: 1; }
  .fold { fill: none; stroke: var(--fold); stroke-width: 1; stroke-dasharray: 4 3; }
  .dim-line { stroke: var(--dim); stroke-width: 1; }
  .dim-arrow { fill: #8a8a3a; }
  .dim-label { font-family: "Oswald", sans-serif; font-weight: 600; font-size: 17px; fill: var(--ink); }
  .panel-light { fill: var(--panel-light); }
  .panel-dark { fill: var(--panel-dark); }
  .title { font-family: "Orbitron", sans-serif; font-weight: 600; font-size: 19px; text-anchor: middle; }
  .title--back { fill: var(--ink); }
  .title--front { fill: var(--accent-orange); }
  .title--side { fill: var(--white); font-size: 21px; }
  .pill-label { font-family: "Open Sans", sans-serif; font-size: 15px; fill: var(--white); }
  .spec-head { font-family: "Open Sans", sans-serif; font-weight: 700; font-size: 13px; fill: var(--ink); }
  .spec { font-family: "Open Sans", sans-serif; font-size: 13px; fill: var(--ink); }
  .feature { font-family: "Lora", serif; font-size: 12px; fill: var(--white); }
  .feature-dot { fill: var(--accent-yellow); }
  .model { font-family: "Oswald", sans-serif; font-weight: 600; font-size: 10px; fill: var(--white); }
  .window-frame { fill: var(--white); stroke: var(--cut); stroke-width: 1; }
</style>
</head>
<body>
<svg class="dieline" viewBox="0 0 1200 1000" xmlns="http://www.w3.org/2000/svg">
  <defs>
    <linearGradient id="window-sky" x1="0" y1="0" x2="1" y2="0">
      <stop offset="0" stop-color="var(--sky-mid)"/>
      <stop offset="0.7" stop-color="var(--sky-mid)"/>
      <stop offset="1" stop-color="var(--sky-edge)"/>
    </linearGradient>
    <linearGradient id="product-tones" x1="0" y1="0" x2="1" y2="1">
      <stop offset="0" stop-color="#e8eaee"/>
      <stop offset="1" stop-color="#d6d8dd"/>
    </linearGradient>
  </defs>

  <!-- Dimension lines -->
  <g class="dimensions">
    <line class="dim-line" x1="80" y1="48" x2="80" y2="958"/>
    <polygon class="dim-arrow" points="80,44 77,58 83,58"/>
    <polygon class="dim-arrow" points="80,962 77,948 83,948"/>
    <text class="dim-label" transform="translate(95 505) rotate(-90)" text-anchor="middle">256.00</text>
    <line class="dim-line" x1="102" y1="962" x2="1073" y2="962"/>
    <polygon class="dim-arrow" points="98,962 112,959 112,965"/>
    <polygon class="dim-arrow" points="1077,962 1063,959 1063,965"/>
    <text class="dim-label" x="587" y="970" text-anchor="middle">274.00</text>
  </g>

  <!-- Back panel with top dust flap -->
  <g class="back">
    <path class="cut" d="M108 224 V96 H418 V224"/>
    <rect class="cut" x="172" y="152" width="191" height="14" rx="7"/>
    <rect class="panel-light" x="105" y="224" width="315" height="528"/>
    <path class="cut" d="M105 224 V752 H420"/>
    <line class="fold" x1="105" y1="224" x2="420" y2="224"/>
    <path class="cut" d="M160 224 V230 M365 224 V230"/>
    <text class="title title--back" x="258" y="274">Customizable Stereo</text>
    <text class="title title--back" x="258" y="296">In-Ear Earphones</text>
    <rect x="140" y="312" width="272" height="192" fill="url(#product-tones)" role="img" aria-label="Product photo: in-ear earphones with swappable yellow caps and the multifunctional controller"/>
    <path fill="var(--pill)" d="M198 505 H420 V538 H198 A16.5 16.5 0 0 1 198 505 Z"/>
    <text class="pill-label" x="200" y="527">Multifunctional Controller</text>
    <text class="spec-head" x="185" y="565">Contents</text>
    <text class="spec" x="183" y="582">2 Pairs of Switchable Caps</text>
    <text class="spec" x="183" y="599">3 Pairs of Silicone Ear tips</text>
    <text class="spec-head" x="183" y="623">User Manual</text>
    <text class="spec-head" x="184" y="646">Specification:</text>
    <text class="spec" x="184" y="666">Frequency Response: 20</text>
    <text class="spec" x="184" y="683">Sensitivity: 105</text>
    <text class="spec" x="184" y="701">THD: &lt;3%</text>
    <text class="spec" x="184" y="719">Cord Length: 3.6ft</text>
  </g>

  <!-- Left side panel -->
  <g class="side side--left">
    <path class="cut" d="M420 224 L428 214 V100 H437 V110 L444 110 V100 H480 V150 A8 8 0 0 0 496 150 V100 H540 V210 L548 224"/>
    <rect class="panel-dark" x="420" y="224" width="135" height="528"/>
    <path class="cut" d="M420 752 V885 H548 V762 L555 752"/>
    <text class="title title--side" transform="translate(485 490) rotate(90)">Customizable Stereo</text>
    <text class="title title--side" transform="translate(460 490) rotate(90)">In-Ear Earphones</text>
  </g>

  <!-- Front panel with window -->
  <g class="front">
    <path class="cut" d="M556 224 V92 H610 V62 A26 26 0 0 1 636 36 H786 A26 26 0 0 1 812 62 V92 H866 V224"/>
    <line class="fold" x1="610" y1="92" x2="812" y2="92"/>
    <rect class="cut" x="620" y="150" width="188" height="14" rx="7"/>
    <rect class="panel-dark" x="555" y="224" width="313" height="528"/>
    <line class="fold" x1="555" y1="224" x2="868" y2="224"/>
    <line class="fold" x1="555" y1="224" x2="555" y2="752"/>
    <line class="fold" x1="868" y1="224" x2="868" y2="752"/>
    <text class="title title--front" x="712" y="264">Customizable Stereo</text>
    <text class="title title--front" x="712" y="288">In-Ear Earphones</text>
    <rect class="window-frame" x="517" y="308" width="389" height="374" rx="12"/>
    <rect x="555" y="308" width="313" height="374" fill="url(#window-sky)" role="img" aria-label="Window view: white controller with call button, white and orange earbuds and a yellow emoji cap"/>
    <g class="features">
      <rect class="feature-dot" x="574" y="692" width="8" height="8"/>
      <text class="feature" x="588" y="700">Customizable earbuds</text>
      <rect class="feature-dot" x="574" y="711" width="8" height="8"/>
      <text class="feature" x="588" y="719">Silicone Gel Ear tips</text>
      <rect class="feature-dot" x="574" y="730" width="8" height="8"/>
      <text class="feature" x="588" y="738">Ergonomic Design</text>
      <rect class="feature-dot" x="746" y="694" width="8" height="8"/>
      <text class="feature" x="760" y="702">In Line Mic</text>
      <rect class="feature-dot" x="746" y="712" width="8" height="8"/>
      <text class="feature" x="760" y="720">3.5mm Jack</text>
      <text class="model" x="746" y="740">MODEL NUMBER: SC-1</text>
    </g>
    <path class="cut" d="M556 752 V940 A0 0 0 0 0 556 940 M556 885 V915 A26 26 0 0 0 582 940 H840 A26 26 0 0 0 866 915 V752"/>
    <line class="fold" x1="586" y1="885" x2="838" y2="885"/>
  </g>

  <!-- Right side panel and glue flap -->
  <g class="side side--right">
    <path class="cut" d="M868 224 L876 214 V100 H933 V150 A8 8 0 0 0 949 150 V100 H998 V210 L1000 224"/>
    <rect class="panel-dark" x="868" y="224" width="132" height="528"/>
    <path class="cut" d="M868 752 L876 762 V885 H1000 V752"/>
    <path class="cut" d="M1000 224 L1075 238 V738 L1000 752"/>
    <line class="fold" x1="1000" y1="224" x2="1000" y2="752"/>
    <text class="title title--side" transform="translate(946 490) rotate(-90)">Customizable Stereo</text>
    <text class="title title--side" transform="translate(971 490) rotate(-90)">In-Ear Earphones</text>
  </g>
</svg>
</body>
</html>
```